Business Card needed for Drainor, a growing Septic Service company

Drainor, a growing local septic service company in Pennsylvania, needs updated business cards. We'd like the business card to feature our logo and communicate that we provide Septic Pumping, Installations/Repairs, Restroom Rentals, and 24/7 Emergency Service. The business card should be eye-catching, bold, and clean/simple. We have been in business almost 10 years and would like to expand and update our business brand and image.

Target Market(s)

Residential and Commercial, New and Current Homeowners

Industry/Entity Type

Service

Contact Information for Business Card

Contact on the business card should be: Dean Harlow Owner & Operator
Phone: 610-555-0187
Email: service@drainor-example.com
Website: www.drainor-example.com
Address: 812 Millbrook Lane Easton PA 18042

Font styles to use
Sans Serif

Colors

Designer to choose colors to be used in the design.

Requirements
Must have
• Feature logo on both side of business card.
Nice to have
• We envision the contact information on one side and our services listed on the other side. Utilize the green from the symbol in our logo as part of the design, overall design color scheme should be white, grey, black.

```html
<!DOCTYPE html>
<html lang="en">
<head>
<meta charset="utf-8">
<title>Drainor Business Card</title>
<link href="https://fonts.googleapis.com/css2?family=Arimo:wght@400;700&family=Oswald:wght@600&family=Open+Sans:wght@400&display=swap" rel="stylesheet">
<style>
  :root {
    --backdrop: #ebeceb;
    --paper: #ffffff;
    --ink: #1d1c19;
    --green-light: #8dc02b;
    --green-deep: #0aa14a;
    --text-light: #ffffff;
  }
  * { margin: 0; padding: 0; box-sizing: border-box; }
  html, body {
    width: 1200px; height: 1091px; overflow: hidden;
    background: var(--backdrop);
    font-family: "Arimo", Arial, sans-serif;
  }
  .card {
    position: absolute;
    width: 704px; height: 407px;
    background: var(--paper);
    border-radius: 22px;
    overflow: hidden;
    box-shadow: 18px 22px 26px rgba(0,0,0,0.18);
  }
  .card-front { left: 148px; top: 99px; }
  .card-back { left: 342px; top: 593px; }
  .card-art { position: absolute; inset: 0; width: 704px; height: 407px; }

  .brand {
    position: absolute;
    display: flex; align-items: center; gap: 8px;
  }
  .brand-square {
    width: 42px; height: 42px;
    background: var(--green-light);
  }
  .brand-name {
    font-family: "Arimo", Arial, sans-serif;
    font-weight: 700;
    font-size: 40px;
    letter-spacing: 2px;
    color: var(--ink);
    line-height: 1;
  }
  .card-front .brand { left: 41px; top: 131px; }
  .card-back .brand { left: 400px; top: 49px; }
  .card-back .brand-square { width: 45px; height: 45px; }

  .holder { position: absolute; left: 51px; top: 210px; }
  .holder-name {
    font-family: "Oswald", "Arial Narrow", sans-serif;
    font-weight: 600;
    font-size: 39px;
    line-height: 1;
    color: var(--green-light);
  }
  .holder-role {
    font-family: "Open Sans", Arial, sans-serif;
    font-size: 21px;
    color: var(--ink);
    margin-top: 4px;
    letter-spacing: 0.3px;
  }

  .contact-list { position: absolute; left: 356px; top: 228px; list-style: none; }
  .contact-item {
    display: flex; align-items: center;
    height: 29.5px;
    color: var(--text-light);
    font-size: 18px;
  }
  .contact-icon { width: 16px; height: 16px; margin-right: 12px; flex: none; }

  .service-list { position: absolute; left: 33px; top: 222px; list-style: none; }
  .service-item {
    display: flex; align-items: center;
    height: 37.5px;
    color: var(--text-light);
    font-size: 27px;
  }
  .service-item::before {
    content: "";
    width: 10px; height: 10px;
    background: var(--green-light);
    margin-right: 8px;
    flex: none;
  }
</style>
</head>
<body>

<section class="card card-front">
  <svg class="card-art" viewBox="0 0 1182 683" preserveAspectRatio="none" aria-hidden="true">
    <defs>
      <linearGradient id="swoosh-front" x1="0" y1="0" x2="0" y2="1">
        <stop offset="0.35" stop-color="#8dc02b"/>
        <stop offset="1" stop-color="#0aa14a"/>
      </linearGradient>
    </defs>
    <path fill="url(#swoosh-front)" d="M1180,20 C800,30 467,250 467,528 C467,600 480,640 499,683 L554,683 C535,640 523,600 523,528 C523,280 820,40 1180,20 Z"/>
    <path fill="var(--ink)" d="M1182,25 C830,35 548,270 548,528 C548,600 560,640 578,683 L1182,683 Z"/>
  </svg>

  <div class="brand">
    <span class="brand-square"></span>
    <span class="brand-name">DRAINOR</span>
  </div>

  <div class="holder">
    <h1 class="holder-name">DEAN HARLOW</h1>
    <p class="holder-role">Owner &amp; Operator</p>
  </div>

  <ul class="contact-list">
    <li class="contact-item">
      <svg class="contact-icon" viewBox="0 0 16 16" aria-hidden="true"><path fill="#fff" d="M1 6 C1 3 15 3 15 6 L15 7 L11 7 L11 5.5 L5 5.5 L5 7 L1 7 Z M4 8 L12 8 L14 14 L2 14 Z"/></svg>
      610-555-0187
    </li>
    <li class="contact-item">
      <svg class="contact-icon" viewBox="0 0 16 16" aria-hidden="true"><rect x="1.5" y="3.5" width="13" height="9" fill="none" stroke="#fff" stroke-width="1.6"/><path d="M2 4 L8 9 L14 4" fill="none" stroke="#fff" stroke-width="1.6"/></svg>
      service@drainor-example.com
    </li>
    <li class="contact-item">
      <svg class="contact-icon" viewBox="0 0 16 16" aria-hidden="true"><g fill="none" stroke="#fff" stroke-width="1.2"><circle cx="8" cy="8" r="6.5"/><ellipse cx="8" cy="8" rx="3" ry="6.5"/><path d="M1.5 8 H14.5 M2.5 5 H13.5 M2.5 11 H13.5"/></g></svg>
      www.drainor-example.com
    </li>
    <li class="contact-item">
      <svg class="contact-icon" viewBox="0 0 16 16" aria-hidden="true"><path fill="#fff" d="M8 1 C4.7 1 3 3.4 3 5.8 C3 9 8 15 8 15 C8 15 13 9 13 5.8 C13 3.4 11.3 1 8 1 Z"/><circle cx="8" cy="6" r="2" fill="var(--ink)"/></svg>
      812 Millbrook Lane Easton, PA 18042
    </li>
  </ul>
</section>

<section class="card card-back">
  <svg class="card-art" viewBox="0 0 1182 683" preserveAspectRatio="none" aria-hidden="true">
    <defs>
      <linearGradient id="swoosh-back" x1="0" y1="0" x2="0" y2="1">
        <stop offset="0.35" stop-color="#8dc02b"/>
        <stop offset="1" stop-color="#0aa14a"/>
      </linearGradient>
    </defs>
    <path fill="url(#swoosh-back)" d="M5,23 C380,30 715,250 715,528 C715,600 702,640 683,683 L628,683 C647,640 658,600 658,528 C658,280 370,30 5,23 Z"/>
    <path fill="var(--ink)" d="M0,28 C350,35 634,270 634,528 C634,600 622,640 605,683 L0,683 Z"/>
  </svg>

  <div class="brand">
    <span class="brand-square"></span>
    <span class="brand-name">DRAINOR</span>
  </div>

  <ul class="service-list">
    <li class="service-item">Septic Pumping</li>
    <li class="service-item">Installations/Repairs</li>
    <li class="service-item">Restroom Rentals</li>
    <li class="service-item">24/7 Emergency Service</li>
  </ul>
</section>

</body>
</html>
```